Client Proposal

I need a proposal template to give to potential clients detailing our services, safety, company history, table of contents and appendixes. I need a cover page to start with images describing our services. Our company is based in Grande Prairie, Alberta. We do land survey work, engineering and environmental.

In word format please so that we can change the proposal on an as needed basis.

```html
<!DOCTYPE html>
<html lang="en">
<head>
<meta charset="utf-8">
<title>Project Proposal 2020 – Northline Group</title>
<link href="https://fonts.googleapis.com/css2?family=Lato:wght@300;400;700;900&display=swap" rel="stylesheet">
<style>
  :root{
    --backdrop:#cccccc;
    --brand-blue:#1597cd;
    --brand-grey:#858a8f;
    --ink:#333a40;
    --paper:#ffffff;
    --sky-top:#8fcde9;
    --sky-bottom:#f4f8fb;
    --field:#b59a6a;
  }
  html,body{margin:0;padding:0;width:667px;height:1200px;overflow:hidden;background:var(--backdrop);}
  body{position:relative;font-family:'Lato',sans-serif;color:var(--ink);}
  .page{position:absolute;left:189px;width:618px;height:800px;transform-origin:0 0;transform:scale(.4661);background:var(--paper);overflow:hidden;}
  .page--cover{top:27px;}
  .page--contents{top:414px;}
  .page--intro{top:801px;}

  /* cover */
  .cover-art{position:absolute;inset:0;}
  .cover-brand{position:absolute;left:55px;top:55px;display:flex;align-items:center;gap:10px;font:900 26px/1 'Lato',sans-serif;color:var(--brand-blue);letter-spacing:.5px;}
  .cover-brand .mark{width:22px;height:22px;background:var(--brand-blue);}
  .cover-title{position:absolute;left:259px;top:566px;color:var(--paper);font-family:'Lato',sans-serif;}
  .cover-title .strong{display:block;font-weight:900;font-size:50px;line-height:47px;}
  .cover-title .year{display:block;font-weight:400;font-size:50px;line-height:50px;}

  /* running header / footer */
  .page-header{position:absolute;left:0;top:0;width:618px;height:72px;background:var(--brand-blue);}
  .header-brand{position:absolute;left:48px;top:24px;display:flex;align-items:center;gap:8px;font:700 18px/1 'Lato',sans-serif;color:var(--paper);letter-spacing:.5px;}
  .header-brand .mark{width:16px;height:16px;background:var(--paper);}
  .header-site{position:absolute;right:48px;top:28px;font:700 12px/1 'Lato',sans-serif;color:var(--paper);}
  .page-footer{position:absolute;left:0;top:740px;width:618px;height:35px;}
  .page-footer svg{position:absolute;inset:0;}
  .footer-title{position:absolute;left:48px;top:11px;font:700 12px/1 'Lato',sans-serif;color:var(--paper);}
  .footer-title span{font-weight:400;}
  .footer-number{position:absolute;left:560px;top:11px;font:700 12px/1 'Lato',sans-serif;color:var(--paper);}

  /* contents page */
  .sky{position:absolute;left:0;top:72px;width:618px;height:310px;background:linear-gradient(var(--sky-top),var(--sky-bottom) 80%);}
  .aerial{position:absolute;left:0;top:375px;width:618px;height:425px;background:linear-gradient(#dfe3e0 0%,#c9b896 10%,#b49a6b 45%,#9a8a5e 75%,#8a8058 100%);}
  .page-heading{position:absolute;left:0;width:618px;text-align:center;font:700 18px/1 'Lato',sans-serif;margin:0;}
  .contents-heading{top:124px;color:var(--ink);}
  .contents-list{position:absolute;left:146px;top:180px;width:322px;margin:0;padding:0;list-style:none;}
  .contents-list li{display:flex;justify-content:space-between;font:400 12px/22px 'Lato',sans-serif;color:var(--ink);}

  /* intro page */
  .intro-heading{top:124px;color:var(--brand-blue);}
  .who-title{position:absolute;left:49px;top:170px;margin:0;font:700 15px/1 'Lato',sans-serif;color:var(--ink);}
  .who-text{position:absolute;left:49px;top:195px;width:528px;margin:0;font:400 10.3px/13.4px 'Lato',sans-serif;}
  .section-title{position:absolute;left:47px;top:315px;margin:0;font:700 15.5px/20px 'Lato',sans-serif;color:var(--brand-blue);}
  .column{position:absolute;top:378px;width:250px;font:400 10.3px/13.4px 'Lato',sans-serif;}
  .column--left{left:49px;}
  .column--right{left:323px;}
  .column p{margin:0 0 13px;}
  .column h3{margin:0;font:700 13px/15px 'Lato',sans-serif;color:var(--ink);}
</style>
</head>
<body>

<!-- Cover -->
<section class="page page--cover">
  <svg class="cover-art" viewBox="0 0 618 800" width="618" height="800">
    <defs>
      <linearGradient id="site" x1="0" y1="0" x2="0.6" y2="1">
        <stop offset="0" stop-color="#c4d6e2"/>
        <stop offset=".45" stop-color="#e8c9a0"/>
        <stop offset="1" stop-color="#9a6a3e"/>
      </linearGradient>
      <linearGradient id="plans" x1="0" y1="0" x2="1" y2="1">
        <stop offset="0" stop-color="#e9f1f8"/>
        <stop offset="1" stop-color="#9fb9d6"/>
      </linearGradient>
    </defs>
    <polygon points="0,110 118,300 0,372" fill="var(--brand-grey)"/>
    <polygon points="0,372 124,306 250,562 60,650 0,545" fill="url(#plans)" role="img" aria-label="Photo of hands drafting on an engineering plan"/>
    <path d="M124,306 L575,62 Q610,48 618,90 L618,330 L250,562 Z" fill="url(#site)" role="img" aria-label="Photo of a surveyor with a total station on a construction site with a crane"/>
    <polygon points="0,545 60,650 618,330 618,800 0,800" fill="var(--brand-blue)"/>
    <g fill="none" stroke="#ffffff" stroke-opacity=".45" stroke-width="1.2">
      <path d="M285,20 Q270,40 290,70 L400,250"/>
      <path d="M300,0 L618,0"/>
      <path d="M0,220 L45,285 Q55,298 75,292 L118,280"/>
      <path d="M480,400 L618,640"/>
      <path d="M430,560 Q420,540 440,528 L618,430"/>
      <path d="M440,560 L545,800"/>
    </g>
  </svg>
  <div class="cover-brand"><span class="mark"></span>NORTHLINE GROUP</div>
  <h1 class="cover-title"><span class="strong">PROJECT</span><span class="strong">PROPOSAL</span><span class="year">2020</span></h1>
</section>

<!-- Table of contents -->
<section class="page page--contents">
  <div class="sky"></div>
  <div class="aerial" role="img" aria-label="Aerial photo of a rural town spreading over open farmland"></div>
  <header class="page-header">
    <div class="header-brand"><span class="mark"></span>NORTHLINE GROUP</div>
    <div class="header-site">northlinegroup.ca</div>
  </header>
  <h2 class="page-heading contents-heading">TABEL OF CONTENT</h2>
  <ul class="contents-list">
    <li><span>Table of Contents</span><span>2</span></li>
    <li><span>An Introduction</span><span>3</span></li>
    <li><span>Company History</span><span>4</span></li>
    <li><span>Our Services</span><span>5</span></li>
    <li><span>Safety</span><span>6</span></li>
    <li><span>Appendixes</span><span>7</span></li>
  </ul>
  <footer class="page-footer">
    <svg viewBox="0 0 618 35" width="618" height="35">
      <polygon points="0,0 536,0 514,35 0,35" fill="var(--brand-grey)"/>
      <polygon points="548,0 618,0 618,35 526,35" fill="var(--brand-blue)"/>
    </svg>
    <div class="footer-title">PROJECT PROPOSAL <span>2020</span></div>
    <div class="footer-number">2</div>
  </footer>
</section>

<!-- Introduction -->
<section class="page page--intro">
  <header class="page-header">
    <div class="header-brand"><span class="mark"></span>NORTHLINE GROUP</div>
    <div class="header-site">northlinegroup.ca</div>
  </header>
  <h2 class="page-heading intro-heading">AN INTRODUCTION</h2>
  <h3 class="who-title">Who We Are</h3>
  <p class="who-text">Northline Group is a partnership between Northline Geomatics Inc, in operation since July 2013, and the recently formed Northline Engineering Inc. Northline Geomatics experienced steady growth throughout Alberta since opening for business. The addition of Northline Engineering in January 2016 and led by two senior civil engineers with extensive experience in the Peace Region, makes Northline Group uniquely positioned to offer fully integrated, professional surveying and civil engineering solutions, creating cost effective, innovative outcomes for our clients.</p>
  <h2 class="section-title">PROFESSIONALS,<br>PARTNERSHIPS &amp; PROCESS</h2>
  <div class="column column--left">
    <p>At Northline Group Surveying &amp; Engineering, we cultivate a culture that guarantees the best outcomes for your projects every time. This culture starts with a passionate desire to be in partnership with our customers, our colleagues and our communities across Alberta. We aim to offer solutions for any surveying or civil engineering task or project.</p>
    <h3>Our Approach is Partnership &amp; Innovation</h3>
    <p>We work with our clients in consultation and partnership on every project to truly understand your technical needs and expectations (and your budget). Creating successful outcomes with our customers is a fundamental part of our business philosophy and a very rewarding aspect of our work.</p>
    <p>Our professional and technical staff treats every task, from traditional to ‘never been done before’, with best practices and mindset of seeking</p>
  </div>
  <div class="column column--right">
    <p>constant innovation. This means we can use our innovative technology, integrated services and tested processes to deliver exceptional results, beyond your expectations, every time.</p>
    <h3>Commitment to Safety</h3>
    <p>Northline Group has been awarded a Certificate of Recognition (COR) for our safety program. We are devoted to safe work practices and environments for all employees, contractors, subcontractors, clients and the communities where we conduct our business. The well-being of the environment is elemental in our philosophy.</p>
    <h3>Where We Operate</h3>
    <p>We offer a broad scope of Surveying and Civil Engineering services from our offices across Alberta. From the Peace Country to the Southern Foothills and all points in between we offer services to nearly all sectors of industry.</p>
  </div>
  <footer class="page-footer">
    <svg viewBox="0 0 618 35" width="618" height="35">
      <polygon points="0,0 536,0 514,35 0,35" fill="var(--brand-grey)"/>
      <polygon points="548,0 618,0 618,35 526,35" fill="var(--brand-blue)"/>
    </svg>
    <div class="footer-title">PROJECT PROPOSAL <span>2020</span></div>
    <div class="footer-number">3</div>
  </footer>
</section>

</body>
</html>
```